Business Card for By Marcus Hale

Looking to have a business card designed for my lifestyle and fitness company. My company offers personal training, online programming and nutrition advice based out of London, United Kingdom.

I'd like to see modern, sleek designs, focusing on black, matte black or matte grey. Design doesn't need to be overly descriptive as this will also be used as a personal business card. I've included my logo.

Please note that my company is no longer called "Fitness by Marcus Hale" but instead "By Marcus Hale", this is because of my other ventures. Therefore please don't use the "fitness by marcus hale" text.

information about my company can be found at www.bymarcushale.com

Company is also based out of London (United Kingdom) & Sydney (Australia) this could be reflected on the card.

Industry/Entity Type

Business

Contact Information for Business Card

Marcus Hale
+44 7382 615204
marcus@bymarcushale.com
www.bymarcushale.com

Font styles to use
Sans Serif

Requirements
Must have
• All contact details and inclusion of my logo.

```html
<!DOCTYPE html>
<html lang="en">
<head>
<meta charset="utf-8">
<title>By Marcus Hale — Business Card</title>
<link rel="stylesheet" href="https://fonts.googleapis.com/css2?family=Oswald:wght@400;500&family=Work+Sans:wght@400&display=swap">
<style>
  :root {
    --backdrop: #1d1d1f;
    --card: #161617;
    --card-edge: #262628;
    --ink: #f4f4f4;
    --ink-muted: #8e8e92;
    --ink-soft: #5c5c60;
  }
  * { margin: 0; padding: 0; box-sizing: border-box; }
  html, body {
    width: 1200px;
    height: 900px;
    overflow: hidden;
    background: var(--backdrop);
  }
  .canvas {
    position: relative;
    width: 1200px;
    height: 900px;
  }
  .card {
    position: absolute;
    left: 290px;
    width: 620px;
    height: 354px;
    background: var(--card);
    border: 1px solid var(--card-edge);
  }
  .card--front { top: 70px; }
  .card--back { top: 476px; }

  /* Front */
  .brand {
    position: absolute;
    left: 0; right: 0;
    top: 86px;
    display: flex;
    flex-direction: column;
    align-items: center;
  }
  .brand__dot {
    width: 74px;
    height: 74px;
    border-radius: 50%;
    background: var(--ink-soft);
    margin-bottom: 26px;
  }
  .brand__name {
    font-family: "Oswald", sans-serif;
    font-weight: 500;
    font-size: 34px;
    letter-spacing: 5px;
    color: var(--ink-muted);
    text-transform: uppercase;
    line-height: 1;
  }
  .brand__cities {
    margin-top: 10px;
    font-family: "Work Sans", sans-serif;
    font-size: 13px;
    letter-spacing: 3px;
    color: var(--ink-soft);
    text-transform: uppercase;
  }

  /* Back */
  .mark {
    position: absolute;
    left: 58px;
    top: 108px;
    width: 120px;
    display: flex;
    flex-direction: column;
    align-items: center;
  }
  .mark__dot {
    width: 62px;
    height: 62px;
    border-radius: 50%;
    background: var(--ink);
    margin-bottom: 12px;
  }
  .mark__name {
    font-family: "Oswald", sans-serif;
    font-weight: 500;
    font-size: 16px;
    letter-spacing: 2px;
    color: var(--ink);
    text-transform: uppercase;
    white-space: nowrap;
  }
  .divider {
    position: absolute;
    left: 206px;
    top: 92px;
    width: 2px;
    height: 122px;
    background: var(--ink);
  }
  .contact {
    position: absolute;
    left: 236px;
    top: 96px;
  }
  .contact__name {
    font-family: "Oswald", sans-serif;
    font-weight: 500;
    font-size: 38px;
    letter-spacing: 3px;
    color: var(--ink);
    text-transform: uppercase;
    line-height: 1;
    margin-bottom: 18px;
  }
  .contact__list { list-style: none; }
  .contact__item {
    display: flex;
    align-items: center;
    gap: 10px;
    font-family: "Work Sans", sans-serif;
    font-size: 17px;
    color: var(--ink);
    line-height: 24px;
  }
  .contact__icon {
    width: 12px;
    height: 12px;
    flex: none;
  }
</style>
</head>
<body>
<main class="canvas">

  <section class="card card--front" aria-label="Card front">
    <div class="brand">
      <div class="brand__dot"></div>
      <div class="brand__name">Marcus Hale</div>
      <div class="brand__cities">London · Sydney</div>
    </div>
  </section>

  <section class="card card--back" aria-label="Card back">
    <div class="mark">
      <div class="mark__dot"></div>
      <div class="mark__name">Marcus Hale</div>
    </div>
    <div class="divider"></div>
    <div class="contact">
      <h1 class="contact__name">Marcus Hale</h1>
      <ul class="contact__list">
        <li class="contact__item">
          <svg class="contact__icon" viewBox="0 0 12 12" aria-hidden="true">
            <path d="M2.5 1 L4.5 1 L5.2 3.6 L4 4.6 C4.6 5.9 6 7.3 7.4 8 L8.4 6.8 L11 7.5 L11 9.5 C11 10.3 10.3 11 9.5 11 C5 11 1 7 1 2.5 C1 1.7 1.7 1 2.5 1 Z" fill="#f4f4f4"/>
          </svg>
          +44 7382 615204
        </li>
        <li class="contact__item">
          <svg class="contact__icon" viewBox="0 0 12 12" aria-hidden="true">
            <rect x="1" y="2.5" width="10" height="7" fill="none" stroke="#f4f4f4" stroke-width="1"/>
            <path d="M1 2.5 L6 6.5 L11 2.5" fill="none" stroke="#f4f4f4" stroke-width="1"/>
          </svg>
          marcus@bymarcushale.com
        </li>
        <li class="contact__item">
          <svg class="contact__icon" viewBox="0 0 12 12" aria-hidden="true">
            <circle cx="6" cy="6" r="5" fill="none" stroke="#f4f4f4" stroke-width="1"/>
            <ellipse cx="6" cy="6" rx="2.2" ry="5" fill="none" stroke="#f4f4f4" stroke-width="0.9"/>
            <path d="M1 6 H11 M2 3.5 H10 M2 8.5 H10" stroke="#f4f4f4" stroke-width="0.8"/>
          </svg>
          www.bymarcushale.com
        </li>
      </ul>
    </div>
  </section>

</main>
</body>
</html>
```